Vantrel Consulting Business card design.

See our website www.vantrelconsulting.com which will give you a good idea of what we are about. The font is called 'Play'.

I'd like a standout business card in keeping with the themes and branding on the website

Target Market(s)

professionals. HR directors

Industry/Entity Type

Business

Contact Information for Business Card

Vantrel Consulting PO Box 3917 Marrowdene NSW 2279 1300 584 316 Gareth Lindqvane Principal email: career@vantrelconsulting.com ABN: 41293087614

Other font styles liked:
• Play

Requirements
Must have
• Must have same design colours and branding as website.
• On back I'd prefer a list of the things we do which appears below the name at the header on the website

```html
<!DOCTYPE html>
<html lang="en">
<head>
<meta charset="utf-8">
<title>Vantrel Consulting – Business Card</title>
<link rel="stylesheet" href="https://fonts.googleapis.com/css2?family=Open+Sans:wght@400;600;700&display=swap">
<style>
  :root {
    --brand-red: #b01e23;
    --brand-grey: #8e8e8e;
    --ink-white: #ffffff;
    --card-white: #ffffff;
    --backdrop: #e4e4e4;
    --card-shadow: rgba(0, 0, 0, 0.14);
  }
  * { box-sizing: border-box; margin: 0; padding: 0; }
  html, body {
    width: 1200px;
    height: 900px;
    overflow: hidden;
    background: var(--backdrop);
    font-family: "Open Sans", Arial, sans-serif;
  }
  .sheet {
    width: 1200px;
    height: 900px;
    display: flex;
    flex-direction: column;
    align-items: center;
    justify-content: center;
    gap: 44px;
  }
  .card {
    position: relative;
    width: 600px;
    height: 343px;
    background: var(--card-white);
    box-shadow: 0 6px 18px var(--card-shadow);
    overflow: hidden;
  }

  /* Front */
  .card--front {
    display: flex;
    align-items: center;
    justify-content: center;
    gap: 16px;
  }
  .brand-dot {
    width: 16px;
    height: 16px;
    border-radius: 50%;
    background: var(--brand-grey);
  }
  .brand-name {
    font-size: 34px;
    font-weight: 600;
    color: var(--brand-red);
    letter-spacing: 1px;
  }

  /* Back */
  .card-shapes {
    position: absolute;
    inset: 0;
    width: 100%;
    height: 100%;
  }
  .back-brand {
    position: absolute;
    left: 28px;
    top: 150px;
    width: 210px;
    font-size: 22px;
    font-weight: 600;
    color: var(--brand-red);
    line-height: 1.25;
  }
  .contact {
    position: absolute;
    right: 36px;
    top: 78px;
    text-align: right;
    color: var(--ink-white);
    font-size: 15px;
    line-height: 1.3;
  }
  .contact__name { font-size: 19px; font-weight: 700; }
  .contact__title { margin-bottom: 16px; }
  .contact__abn { margin-bottom: 12px; }
  .contact__address { margin-bottom: 8px; }
  .contact__line {
    display: flex;
    justify-content: flex-end;
    align-items: center;
    gap: 8px;
  }
  .contact__icon { width: 14px; height: 14px; fill: var(--ink-white); }
</style>
</head>
<body>
<main class="sheet">
  <section class="card card--front" aria-label="Card front">
    <span class="brand-dot"></span>
    <span class="brand-name">Vantrel Consulting</span>
  </section>

  <section class="card card--back" aria-label="Card back">
    <svg class="card-shapes" viewBox="0 0 600 343" aria-hidden="true">
      <path d="M248 0 C318 110 300 250 118 343 L150 343 C322 250 340 110 268 0 Z" fill="var(--brand-grey)"/>
      <path d="M272 0 C345 110 330 255 150 343 L600 343 L600 0 Z" fill="var(--brand-red)"/>
      <path d="M266 0 C339 110 324 255 144 343 L150 343 C330 255 345 110 272 0 Z" fill="var(--card-white)"/>
    </svg>

    <div class="back-brand">Vantrel Consulting</div>

    <div class="contact">
      <div class="contact__name">Gareth Lindqvane</div>
      <div class="contact__title">Principal</div>
      <div class="contact__abn">ABN: 41293087614</div>
      <div class="contact__address">PO Box 3917 Marrowdene<br>NSW 2279</div>
      <div class="contact__line">1300 584 316
        <svg class="contact__icon" viewBox="0 0 24 24" aria-hidden="true"><path d="M6.6 10.8a15.1 15.1 0 0 0 6.6 6.6l2.2-2.2a1 1 0 0 1 1-.25 11.4 11.4 0 0 0 3.6.57 1 1 0 0 1 1 1V20a1 1 0 0 1-1 1A17 17 0 0 1 3 4a1 1 0 0 1 1-1h3.5a1 1 0 0 1 1 1c0 1.25.2 2.45.57 3.57a1 1 0 0 1-.25 1z"/></svg>
      </div>
      <div class="contact__line">career@vantrelconsulting.com
        <svg class="contact__icon" viewBox="0 0 24 24" aria-hidden="true"><path d="M2 5h20v14H2z M3.5 6.5 12 13l8.5-6.5z" fill-rule="evenodd"/></svg>
      </div>
    </div>
  </section>
</main>
</body>
</html>
```